Want to incorporate elements of all these items to make an amazing sign to welcome people to the community. The sign is 6x4 and needs to incorporate the following items:

Welcome to Corwick Meadows

Come visit the PRD sales center at 745 thistledown road
High Speed Fiber Internet
Land financing starting at $299 (No credit checks)
Let us build your dream home!
555-284-7390
We like the gold and black design no teal or blue that was another agents design. Some combination of the current sign all the stuff listed above and then design elements that tie into the truck wrap.

Target Market(s)

People visiting the neighborhood

Industry/Entity Type

real estate and construction

Font styles to use
Serif

Colors

Designer to choose colors to be used in the design.

Requirements
Must have
• PRD Home Builders Welcomes you to Corwick Meadows, Let us build your dream home, Phone number, Land financing starting at $299 NO credit checks

```html
<!DOCTYPE html>
<html lang="en">
<head>
<meta charset="utf-8">
<title>Corwick Meadows – Welcome Sign</title>
<link rel="stylesheet" href="https://fonts.googleapis.com/css2?family=Oswald:wght@400;500;600;700&family=Pinyon+Script&display=swap">
<style>
  :root {
    --ink: #151515;
    --ink-soft: #1d1f1c;
    --gold: #c7ad85;
    --gold-light: #f1dcaa;
    --gold-deep: #a88d68;
    --cream: #f3dfae;
    --white: #ffffff;
    --ribbon-text: #161616;
  }
  * { margin: 0; padding: 0; box-sizing: border-box; }
  html, body { width: 1200px; height: 800px; overflow: hidden; background: var(--ink); }
  .sign {
    position: relative;
    width: 1200px;
    height: 800px;
    overflow: hidden;
    font-family: "Oswald", sans-serif;
  }
  .sign__backdrop {
    position: absolute; inset: 0;
    background:
      radial-gradient(ellipse at 20% 30%, rgba(60,70,55,0.35), transparent 55%),
      radial-gradient(ellipse at 80% 60%, rgba(55,62,50,0.3), transparent 55%),
      linear-gradient(180deg, var(--ink-soft), var(--ink));
  }
  .sign__frame {
    position: absolute;
    left: 24px; top: 25px; width: 1145px; height: 747px;
    border: 1px solid var(--gold);
    border-radius: 8px;
  }
  .welcome {
    position: absolute; left: 0; right: 0; top: 40px;
    text-align: center;
    font-family: "Pinyon Script", cursive;
    font-size: 84px;
    color: var(--gold);
    line-height: 1;
  }
  .art { position: absolute; left: 0; top: 0; }
  .community-name {
    font-family: "Oswald", sans-serif;
    font-weight: 700;
    font-size: 156px;
    fill: var(--white);
  }
  .ribbon-text {
    font-family: "Oswald", sans-serif;
    font-weight: 500;
    font-size: 40px;
    fill: var(--ribbon-text);
  }
  .perks {
    position: absolute; left: 60px; top: 438px;
    display: flex; align-items: center;
    font-size: 36px; color: var(--white);
    line-height: 1;
    white-space: nowrap;
  }
  .perk { display: flex; align-items: center; }
  .perk + .perk { margin-left: 27px; }
  .perk__tick { width: 31px; height: 31px; margin-right: 18px; flex: none; }
  .perk__note { font-size: 29px; color: var(--gold); margin-left: 10px; }
  .dream {
    position: absolute; left: 189px; width: 822px; top: 566px;
    text-align: center;
    font-size: 50px; color: var(--gold);
    line-height: 1;
  }
  .call {
    position: absolute; left: 343px; top: 683px;
    display: flex; align-items: center;
    font-size: 51px; color: var(--white);
    line-height: 1;
    white-space: nowrap;
  }
  .call__icon { width: 62px; height: 62px; margin-right: 16px; }
</style>
</head>
<body>
<main class="sign">
  <div class="sign__backdrop" role="img" aria-label="Dark photo of a forest canopy"></div>
  <div class="sign__frame"></div>

  <p class="welcome">Welcome to</p>

  <svg class="art" width="1200" height="800" viewBox="0 0 1200 800">
    <defs>
      <linearGradient id="goldBar" x1="0" x2="1" y1="0" y2="0">
        <stop offset="0" stop-color="#a88d68"/>
        <stop offset="0.5" stop-color="#f1dcaa"/>
        <stop offset="1" stop-color="#a88d68"/>
      </linearGradient>
    </defs>

    <text class="community-name" x="100" y="280" textLength="1000" lengthAdjust="spacingAndGlyphs"
          style="filter: drop-shadow(4px 2px 0 #e6cf9f);">CORWICK MEADOWS</text>

    <polygon points="103,367 190,367 190,313 125,340 110,317" fill="var(--gold)"/>
    <polygon points="1097,367 1010,367 1010,313 1075,340 1090,317" fill="var(--gold)"/>
    <polygon points="159,329 190,313 190,329" fill="var(--gold-deep)"/>
    <polygon points="1041,329 1010,313 1010,329" fill="var(--gold-deep)"/>
    <rect x="159" y="329" width="879" height="66" fill="var(--cream)"/>
    <text class="ribbon-text" x="186" y="378" textLength="828" lengthAdjust="spacingAndGlyphs">Come visit the PRD sales center at 745 THISTLEDOWN road</text>

    <g fill="var(--gold-light)">
      <polygon points="577,518 600,498 623,518 618,518 600,503 582,518"/>
      <rect x="587" y="515" width="26" height="18"/>
    </g>
    <rect x="597" y="522" width="6" height="11" fill="var(--ink)"/>

    <path d="M221,536 H979 Q979,573 1008,573 V620 Q979,620 979,657 H221 Q221,620 192,620 V573 Q221,573 221,536 Z"
          fill="none" stroke="url(#goldBar)" stroke-width="9" stroke-linejoin="round"/>
  </svg>

  <div class="perks">
    <div class="perk">
      <svg class="perk__tick" viewBox="0 0 34 34" aria-hidden="true">
        <circle cx="15" cy="18" r="13" fill="none" stroke="var(--gold)" stroke-width="3"/>
        <path d="M8 17 L14 24 L30 5" fill="none" stroke="var(--gold)" stroke-width="4" stroke-linecap="round" stroke-linejoin="round"/>
      </svg>
      <span>High Speed Fiber Internet</span>
    </div>
    <div class="perk">
      <svg class="perk__tick" viewBox="0 0 34 34" aria-hidden="true">
        <circle cx="15" cy="18" r="13" fill="none" stroke="var(--gold)" stroke-width="3"/>
        <path d="M8 17 L14 24 L30 5" fill="none" stroke="var(--gold)" stroke-width="4" stroke-linecap="round" stroke-linejoin="round"/>
      </svg>
      <span>Land financing starting at $299</span>
      <span class="perk__note">(No credit checks)</span>
    </div>
  </div>

  <p class="dream">LET US BUILD YOUR DREAM HOME!</p>

  <div class="call">
    <svg class="call__icon" viewBox="0 0 64 64" aria-hidden="true">
      <defs>
        <linearGradient id="goldDisc" x1="0" y1="0" x2="1" y2="1">
          <stop offset="0" stop-color="#f1dcaa"/>
          <stop offset="1" stop-color="#a88d68"/>
        </linearGradient>
      </defs>
      <circle cx="32" cy="32" r="30" fill="url(#goldDisc)" stroke="#fff" stroke-width="3"/>
      <path d="M22 17 l6 -2 l4 9 l-4 3 q3 7 9 10 l3 -4 l9 4 l-2 6 q-3 3 -8 2 q-12 -4 -18 -17 q-2 -7 1 -11 Z" fill="#fff"/>
      <path d="M36 20 q6 1 8 8 M37 14 q11 2 13 13" fill="none" stroke="#fff" stroke-width="2.5" stroke-linecap="round"/>
    </svg>
    <span>CALL US: 555-284-7390</span>
  </div>
</main>
</body>
</html>
```